7 P's for Healthcare Companies - Textbook Graphic

Can you create a graphic for me for a medical textbook? The goal is to show 7 critical features of a healthcare startup and the audience is physicians with limited business backgrounds.

Please include a picture of young, male emergency physician in the middle of the graphic. Show them evaluating an idea. Can you surround the physician with bold writing for the seven components, and use brief descriptions and simple images or graphics to illustrate the point?

The image should be somewhat formal, but it's OK to be lighthearded.

The seven P's and brief descriptions include the following:
Product: what is their market solution?
(Intellectual) Property: do they have a patent or trademark?
Product Clearance: how will they get QRB approval and TPW clearance?
Payment: how will they make money?
Pilots: have they applied their product in a healthcare setting?
Physician and Patient feedback: Do doctors and patients like their product?
Publication: do they have evidence their product works?

More detail and information is available at this website: https://brenvolt.com/blog/uncategorized/healthcare-framework/

I will need to own this image

```html
<!DOCTYPE html>
<html lang="en">
<head>
<meta charset="utf-8">
<title>7 P's to evaluate healthcare companies</title>
<link rel="stylesheet" href="https://fonts.googleapis.com/css2?family=Bebas+Neue&family=Montserrat:wght@700;800&family=PT+Sans:wght@400&display=swap">
<style>
  :root {
    --bg-top: #1b2fe3;
    --bg-bottom: #08b0f0;
    --panel: #ffffff;
    --ring: #0b63e6;
    --ring-line: #ffffff;
    --dot: #1a2fd6;
    --icon: #1ea6e6;
    --icon-dark: #0d5fd8;
    --ink: #111111;
    --photo-light: #eef3f9;
    --photo-mid: #c9d9ec;
  }
  html, body {
    margin: 0;
    padding: 0;
    width: 1200px;
    height: 1198px;
    overflow: hidden;
  }
  .canvas {
    position: relative;
    width: 1200px;
    height: 1198px;
    overflow: hidden;
    background: linear-gradient(180deg, var(--bg-top) 0%, #1560ea 45%, var(--bg-bottom) 100%);
  }
  .stage {
    position: absolute;
    left: 0;
    top: 0;
    width: 1500px;
    height: 1500px;
    transform: scale(0.8, 0.79867);
    transform-origin: 0 0;
  }
  .artwork {
    position: absolute;
    left: 0;
    top: 0;
    width: 1500px;
    height: 1500px;
  }
  .brand {
    position: absolute;
    left: 100px;
    top: 105px;
    display: flex;
    align-items: center;
    gap: 18px;
    font-family: "Montserrat", sans-serif;
    font-weight: 700;
    font-size: 76px;
    letter-spacing: -1px;
    color: #ffffff;
  }
  .brand-mark {
    width: 34px;
    height: 34px;
    background: #ffffff;
  }
  .title {
    position: absolute;
    right: 78px;
    top: 62px;
    margin: 0;
    width: 900px;
    text-align: right;
    font-family: "Montserrat", sans-serif;
    font-weight: 800;
    font-size: 49px;
    line-height: 60px;
    letter-spacing: -0.3px;
    color: #ffffff;
    white-space: nowrap;
  }
  .p-item {
    position: absolute;
    text-align: center;
    color: var(--ink);
  }
  .p-heading {
    margin: 0;
    font-family: "Bebas Neue", sans-serif;
    font-weight: 400;
    font-size: 60px;
    line-height: 56px;
    color: #000000;
  }
  .p-body {
    margin: 4px 0 0;
    font-family: "PT Sans", sans-serif;
    font-size: 19px;
    line-height: 21px;
    hyphens: auto;
    -webkit-hyphens: auto;
  }
  .item-property { left: 490px; top: 382px; width: 280px; }
  .item-pilots { left: 807px; top: 406px; width: 300px; }
  .item-process { left: 213px; top: 577px; width: 255px; }
  .item-payment { left: 1098px; top: 642px; width: 290px; }
  .item-product { left: 110px; top: 908px; width: 245px; }
  .item-product .p-body { font-size: 20px; line-height: 25px; }
  .item-publications { left: 1180px; top: 948px; width: 285px; }
  .item-feedback { left: 1062px; top: 1238px; width: 300px; }
  .item-feedback .p-heading { font-size: 50px; line-height: 46px; }
  .item-feedback .p-body { margin-top: 8px; padding: 0 30px; }
</style>
</head>
<body>
<div class="canvas">
  <div class="stage">
    <svg class="artwork" viewBox="0 0 1500 1500" xmlns="http://www.w3.org/2000/svg">
      <g class="panels" fill="var(--panel)">
        <path class="panel-product" d="M74.6,1167.9 A730,730 0 0 1 95.8,762.3 L406.8,869.8 A400,400 0 0 0 395.7,1092 Z"/>
        <path class="panel-process" d="M101.6,743.2 A730,730 0 0 1 362.1,405 L553.3,673.9 A400,400 0 0 0 410.6,859.3 Z"/>
        <path class="panel-property" d="M378.9,393.4 A730,730 0 0 1 769.7,270.1 L776.6,600.1 A400,400 0 0 0 562.5,667.6 Z"/>
        <path class="panel-pilots" d="M790.1,270 A730,730 0 0 1 1234.5,424.8 L1031.3,684.8 A400,400 0 0 0 787.8,600 Z"/>
        <path class="panel-payment" d="M1250.3,437.5 A730,730 0 0 1 1483.5,787.8 L1167.7,883.7 A400,400 0 0 0 1040,691.8 Z"/>
        <path class="panel-publications" d="M1489.2,807.4 A730,730 0 0 1 1479.3,1225.6 L1165.4,1123.6 A400,400 0 0 0 1170.8,894.4 Z"/>
        <path class="panel-feedback" d="M1472.7,1244.9 A730,730 0 0 1 1034.7,1686 L921.8,1375.9 A400,400 0 0 0 1161.8,1134.2 Z"/>
      </g>

      <path class="ring-band" fill="var(--ring)" d="M395.7,1092 A400,400 0 1 1 1131.4,1200 L1053.5,1155 A310,310 0 1 0 483.3,1071.3 Z"/>
      <path class="ring-line" fill="none" stroke="var(--ring-line)" stroke-width="3" d="M450.2,1059 A340,340 0 1 1 1093.1,1143.7"/>

      <g class="ring-ticks" stroke="var(--ring-line)" stroke-width="3">
        <line x1="446.3" y1="970.4" x2="386.5" y2="965.1"/>
        <line x1="496.7" y1="819.8" x2="445.8" y2="788"/>
        <line x1="679.9" y1="676.7" x2="661.4" y2="619.6"/>
        <line x1="844" y1="665.2" x2="854.4" y2="606.1"/>
        <line x1="1025.4" y1="759.6" x2="1067.8" y2="717.2"/>
        <line x1="1123.7" y1="970.4" x2="1183.5" y2="965.1"/>
        <line x1="1108.4" y1="1105.1" x2="1165.4" y2="1123.6"/>
      </g>
      <g class="ring-dots" fill="var(--dot)" stroke="#ffffff" stroke-width="3">
        <circle cx="446.3" cy="970.4" r="11"/>
        <circle cx="496.7" cy="819.8" r="11"/>
        <circle cx="679.9" cy="676.7" r="11"/>
        <circle cx="844" cy="665.2" r="11"/>
        <circle cx="1025.4" cy="759.6" r="11"/>
        <circle cx="1123.7" cy="970.4" r="11"/>
        <circle cx="1108.4" cy="1105.1" r="11"/>
      </g>

      <g class="product-arrow" stroke="#ffffff" stroke-width="3" fill="none">
        <line x1="255" y1="1125" x2="270" y2="1168"/>
        <polyline points="261,1160 270,1170 276,1157"/>
      </g>

      <defs>
        <linearGradient id="photoTone" x1="0" y1="0" x2="0" y2="1">
          <stop offset="0" stop-color="var(--photo-light)"/>
          <stop offset="1" stop-color="var(--photo-mid)"/>
        </linearGradient>
      </defs>
      <path class="physician-photo" role="img" aria-label="Photo: smiling young male emergency physician in a white coat with a stethoscope, reviewing an idea on a tablet"
            fill="url(#photoTone)" d="M505,1000 A280,280 0 0 1 1065,1000 L1000,1500 L270,1500 L300,1220 Z"/>

      <g class="icon icon-property" fill="var(--icon)">
        <rect x="612" y="330" width="62" height="36" rx="6"/>
        <rect x="600" y="324" width="10" height="48" rx="3"/>
        <rect x="676" y="340" width="20" height="16"/>
        <rect x="694" y="318" width="8" height="38"/>
        <rect x="578" y="344" width="24" height="8"/>
        <rect x="625" y="318" width="6" height="14" fill="var(--icon-dark)"/>
        <rect x="645" y="318" width="6" height="14" fill="var(--icon-dark)"/>
      </g>
      <g class="icon icon-pilots">
        <path fill="var(--icon)" d="M940,395 L930,365 Q960,330 1012,325 Q1008,378 972,405 Z"/>
        <circle cx="978" cy="353" r="11" fill="#ffffff"/>
        <circle cx="978" cy="353" r="6" fill="var(--icon)"/>
        <path fill="var(--icon-dark)" d="M930,365 L912,368 L928,350 L948,348 Z M972,405 L970,422 L988,405 L990,386 Z"/>
        <g stroke="var(--icon)" stroke-width="6" stroke-linecap="round">
          <line x1="918" y1="380" x2="900" y2="392"/>
          <line x1="930" y1="392" x2="906" y2="408"/>
        </g>
      </g>
      <g class="icon icon-process">
        <g fill="none" stroke="var(--icon)" stroke-width="12">
          <path d="M312,500 A40,40 0 0 1 370,484"/>
          <path d="M386,510 A40,40 0 0 1 372,562"/>
          <path d="M320,555 A40,40 0 0 1 308,515"/>
        </g>
        <g fill="var(--icon)">
          <polygon points="366,472 386,490 360,496"/>
          <polygon points="382,560 358,570 366,548"/>
          <polygon points="298,512 312,490 322,516"/>
          <rect x="338" y="507" width="20" height="34" rx="3"/>
          <rect x="331" y="514" width="34" height="20" rx="3"/>
        </g>
      </g>
      <g class="icon icon-payment">
        <rect x="1208" y="520" width="70" height="100" rx="10" fill="var(--icon)"/>
        <g fill="#ffffff">
          <rect x="1234" y="536" width="18" height="6"/>
          <rect x="1240" y="530" width="6" height="18"/>
          <rect x="1220" y="562" width="44" height="6"/>
          <rect x="1220" y="578" width="36" height="6"/>
          <rect x="1220" y="594" width="30" height="6"/>
        </g>
        <circle cx="1272" cy="583" r="17" fill="#ffffff"/>
        <text x="1272" y="594" text-anchor="middle" font-family="Montserrat, sans-serif" font-weight="800" font-size="30" fill="var(--icon)">$</text>
      </g>
      <g class="icon icon-product">
        <path fill="var(--icon)" d="M186,835 L222,823 L258,835 L256,872 Q250,895 222,902 Q192,895 186,872 Z"/>
        <path fill="var(--icon-dark)" d="M222,823 L222,862 L186,862 L186,835 Z"/>
        <g fill="none" stroke="var(--icon)" stroke-width="6">
          <path d="M238,858 L238,880 Q240,896 252,890 L256,868"/>
        </g>
        <circle cx="256" cy="862" r="8" fill="var(--icon)"/>
      </g>
      <g class="icon icon-publications">
        <rect x="1305" y="866" width="60" height="74" rx="4" fill="var(--icon)"/>
        <g fill="#ffffff">
          <rect x="1315" y="880" width="32" height="5"/>
          <rect x="1315" y="894" width="28" height="5"/>
          <rect x="1315" y="908" width="20" height="5"/>
          <rect x="1315" y="922" width="16" height="5"/>
        </g>
        <rect x="1300" y="932" width="70" height="10" rx="3" fill="var(--icon-dark)"/>
        <path fill="var(--icon-dark)" d="M1336,928 L1370,870 L1382,877 L1348,935 L1334,940 Z"/>
      </g>
      <g class="icon icon-feedback">
        <path fill="var(--icon)" d="M1160,1172 H1218 Q1226,1172 1226,1180 V1218 Q1226,1226 1218,1226 H1188 L1172,1236 L1174,1226 H1160 Q1152,1226 1152,1218 V1180 Q1152,1172 1160,1172 Z"/>
        <g fill="#ffffff">
          <rect x="1164" y="1186" width="24" height="5"/>
          <rect x="1164" y="1198" width="32" height="5"/>
          <rect x="1164" y="1210" width="20" height="5"/>
        </g>
        <path fill="var(--icon-dark)" d="M1196,1210 L1222,1168 L1232,1174 L1206,1216 L1194,1220 Z"/>
      </g>
    </svg>

    <div class="brand"><span class="brand-mark"></span><span class="brand-name">Brenvolt</span></div>
    <h1 class="title">7 P’s to evaluate healthcare<br>companies: A framework for<br>physicians</h1>

    <div class="p-item item-property">
      <h2 class="p-heading">Property</h2>
      <p class="p-body">Patents can be obtained for medical devices, pharmaceutical compounds, and digital health assets. These provide protection from knockoff products and also provide companies with a valuable asset.</p>
    </div>
    <div class="p-item item-pilots">
      <h2 class="p-heading">Pilots</h2>
      <p class="p-body">Healthcare startups achieve traction by obtaining early customers. The first product users from physician offices and hospitals provide feedback that can be used to improve the solution before scaling the company.</p>
    </div>
    <div class="p-item item-process">
      <h2 class="p-heading">Process</h2>
      <p class="p-body">While not every health innovation requires QRB clearance, understanding how a product you’re evaluating is regulated is important for assuring patient safety and mitigating potential risk.</p>
    </div>
    <div class="p-item item-payment">
      <h2 class="p-heading">Payment</h2>
      <p class="p-body">This ‘P’ recognizes the cost of the product and how a company is reimbursed. This includes the company cost to product the product.</p>
    </div>
    <div class="p-item item-product">
      <h2 class="p-heading">Product</h2>
      <p class="p-body">The first step is to evaluate the proposed solution and how well it addresses a medical practice pain point. prototype.</p>
    </div>
    <div class="p-item item-publications">
      <h2 class="p-heading">Publications</h2>
      <p class="p-body">Particularly for diagnostics, medical devices, and drugs, track the efficacy of treatment. Sometimes this is internal information, but companies will publish studies related to their product’s performance.</p>
    </div>
    <div class="p-item item-feedback">
      <h2 class="p-heading">Physician/Patient<br>Feedback</h2>
      <p class="p-body">It’s important to evaluate what kind of feedback was sought from patients and physicians as the product was developed.</p>
    </div>
  </div>
</div>
</body>
</html>
```